Business Card Design Project

We are rebranding an existing automotive collision repair business. The business is called harrowell works. I have attached logo but I'm not tied to that. I want to leave this wide open.

I want this card to say we are professional, competent, cutting edge. We are focused on customers and use a lot of the latest technology to make the customer experience different. We sign customers in on Vextabs. Paperwork I signed electronically and updates are sent via text, email, logging on a website or as they wish. I want this innovation and image to come through in our cards

Target Market(s)

60%. Women 40% men. Age 35-60

Industry/Entity Type

Automotive

Requirements
Must have
• The card must have name, title, phone,email, cell, web page

```html
<!DOCTYPE html>
<html lang="en">
<head>
<meta charset="utf-8">
<title>harrowell works — business card</title>
<link rel="stylesheet" href="https://fonts.googleapis.com/css2?family=Michroma&family=Open+Sans:wght@400;700&display=swap">
<style>
  :root {
    --bg-light: #b9c0c3;
    --bg-dark: #7f8a8c;
    --card-white: #ffffff;
    --card-dark: #24272d;
    --card-dark-edge: #1c1e22;
    --band-black: #1d1d1d;
    --lime: #7cc142;
    --lime-light: #9bd24e;
    --lime-deep: #6db530;
    --text-light: #e9ecef;
    --text-muted: #c9ced3;
  }
  * { box-sizing: border-box; margin: 0; padding: 0; }
  html, body { width: 1200px; height: 1000px; overflow: hidden; }
  body {
    background: radial-gradient(ellipse at 25% 20%, var(--bg-light), var(--bg-dark) 85%);
    font-family: "Open Sans", Arial, sans-serif;
    position: relative;
  }
  .card {
    position: absolute;
    left: 250px;
    width: 700px;
    height: 400px;
    overflow: hidden;
    box-shadow: 0 12px 28px rgba(0,0,0,0.35);
  }
  .card--front { top: 70px; background: var(--card-white); }
  .card--back {
    top: 530px;
    background: linear-gradient(100deg, var(--lime-deep) 0%, var(--lime) 30%, var(--lime-light) 55%, var(--lime-deep) 100%);
  }

  /* front */
  .front__brand {
    position: absolute; top: 0; left: 0; right: 0; height: 210px;
    display: flex; align-items: center; justify-content: center;
  }
  .wordmark {
    font-family: "Open Sans", Arial, sans-serif;
    font-weight: 700;
    font-size: 40px;
    color: var(--lime);
    letter-spacing: 0.5px;
  }
  .front__rule {
    position: absolute; top: 210px; left: 0; right: 0;
    height: 4px; background: var(--lime);
  }
  .front__panel {
    position: absolute; top: 214px; left: 0; right: 0; bottom: 0;
    background: linear-gradient(90deg, var(--card-dark-edge), var(--card-dark) 50%, var(--card-dark-edge));
    border-top: 3px dashed #8a8f96;
  }
  .person { position: absolute; left: 48px; top: 88px; }
  .person__name {
    font-family: "Michroma", "Arial Black", sans-serif;
    font-size: 26px; color: var(--lime); font-weight: 400;
  }
  .person__title { font-size: 14px; color: var(--text-light); margin-top: 4px; margin-left: 32px; }
  .contact {
    position: absolute; left: 400px; top: 22px;
    list-style: none; color: var(--text-light); font-size: 15px;
  }
  .contact li { display: flex; align-items: center; height: 27px; }
  .contact svg { width: 18px; height: 18px; margin-right: 14px; fill: var(--lime); }
  .contact .contact__address { padding-left: 32px; font-size: 14px; color: var(--text-muted); }

  /* back */
  .back__band {
    position: absolute; top: 120px; left: 0; right: 0; height: 150px;
    background: var(--band-black);
    display: flex; align-items: center; justify-content: center;
  }
</style>
</head>
<body>

<section class="card card--front" aria-label="Card front">
  <div class="front__brand">
    <span class="wordmark">harrowell works</span>
  </div>
  <div class="front__rule"></div>
  <div class="front__panel">
    <div class="person">
      <p class="person__name">Your Name</p>
      <p class="person__title">YourTitle</p>
    </div>
    <ul class="contact">
      <li>
        <svg viewBox="0 0 24 24" aria-hidden="true"><path d="M6.6 10.8a15.1 15.1 0 0 0 6.6 6.6l2.2-2.2a1 1 0 0 1 1-.25 11.4 11.4 0 0 0 3.6.57 1 1 0 0 1 1 1V20a1 1 0 0 1-1 1A17 17 0 0 1 3 4a1 1 0 0 1 1-1h3.5a1 1 0 0 1 1 1c0 1.25.2 2.45.57 3.57a1 1 0 0 1-.25 1z"/></svg>
        +1 555 204 318
      </li>
      <li>
        <svg viewBox="0 0 24 24" aria-hidden="true"><path d="M2 5h20v2l-10 6L2 7zM2 9l10 6 10-6v10H2z"/></svg>
        hello@harrowellworks.com
      </li>
      <li>
        <svg viewBox="0 0 24 24" aria-hidden="true"><path d="M12 2a10 10 0 1 0 0 20 10 10 0 0 0 0-20zm6.9 6h-3a15 15 0 0 0-1.3-4A8 8 0 0 1 18.9 8zM12 4c.8 1.1 1.5 2.5 1.9 4h-3.8c.4-1.5 1.1-2.9 1.9-4zM4.3 14a8 8 0 0 1 0-4h3.4a16 16 0 0 0 0 4zm.8 2h3a15 15 0 0 0 1.3 4A8 8 0 0 1 5.1 16zm3-8h-3a8 8 0 0 1 4.3-4 15 15 0 0 0-1.3 4zM12 20c-.8-1.1-1.5-2.5-1.9-4h3.8c-.4 1.5-1.1 2.9-1.9 4zm2.3-6H9.7a14 14 0 0 1 0-4h4.6a14 14 0 0 1 0 4zm.3 6a15 15 0 0 0 1.3-4h3a8 8 0 0 1-4.3 4zm1.7-6a16 16 0 0 0 0-4h3.4a8 8 0 0 1 0 4z"/></svg>
        www.harrowellworks.com
      </li>
      <li class="contact__address">48 Foundry Lane, Marsden, USA</li>
    </ul>
  </div>
</section>

<section class="card card--back" aria-label="Card back">
  <div class="back__band">
    <span class="wordmark">harrowell works</span>
  </div>
</section>

</body>
</html>
```